Template design for organic gardening site for ShopVantra platform

We need a template design for our new 'Fen Leaf Naturals' shopvantra site. Fen Leaf Naturals specialises in organic nutrients for gardening plus all equipment needed to grow.
Domain name will be www.fenleafnaturals.co.uk
Colours used should include logo colours, see attached image. Other colours to compliment the greens and lift the feel of the site could be yellow or orange.
Home page design should include, but not limited to the following:
Interactive banner carousel space
A smaller banner advertising space
Featured products
New products
Sale products feature/link
Articles links/feature
+ all standard shopvantra features such as menus, etc
The site will be selling products (these are nutrients) such as:
Pelvarimost
Marsh hare soil tonic
Terrawix
Nuro pods
Stem triumph
Sprout charm
Vel
Flint amber
Moswelder
+ more products and brands
Site layouts we like include:
www.tidemarkaquafarm.co.uk ... A bit old fashioned but cool
www.lanternbeds.co.uk ... Nice but too compact
www.flintamber.com ... Has a nice top half
www.sponsorapod.org.uk ... Nice colours and header
www.penhurstplants.co.uk ... nice layout, but needs image carousel
www.wrenmeal.co.uk ... Nice background and colours
www.thistle.co.uk ... Nice colours and layout
www.danielmorrowhorticulture.com ... Nice layout and header
www.sprivant.co.uk ... Cool colours and shop pages layout is nice
www.aquavenor.co.uk ... One of the best layouts
The site should feel clean, modern and elegant.
Target Market(s)
Indoor and outdoor organic gardeners
Look and feel

```html
<!DOCTYPE html>
<html lang="en">
<head>
<meta charset="utf-8">
<title>Fen Leaf Naturals – Home</title>
<link rel="stylesheet" href="https://fonts.googleapis.com/css2?family=Open+Sans:wght@400;600;700&family=Oswald:wght@500&display=swap">
<style>
:root{
  --green:#7cc242;
  --green-mid:#6ab33a;
  --green-dark:#4c8a2e;
  --orange:#f26b1d;
  --red:#d42b2b;
  --ink:#333;
  --line:#e3e3e3;
  --panel:#ececec;
  --dark:#3d3d3d;
  --foot:#efefef;
  --foot-bottom:#d9d9d9;
}
*{box-sizing:border-box;margin:0;padding:0}
html,body{width:704px;height:1200px;overflow:hidden;background:#fff}
body{position:relative;font-family:"Open Sans",Arial,sans-serif;color:var(--ink)}
.abs{position:absolute}

.topbar{left:0;top:0;width:704px;height:23px;border-bottom:1px solid var(--line);font-size:7.5px;color:#555}
.topbar span{position:absolute;top:7px}
.topbar .sep{color:#ccc}

.brand{display:flex;align-items:center;gap:7px;white-space:nowrap}
.brand .dot{width:12px;height:12px;border-radius:50%;background:var(--green-mid);flex:none}
.brand .name{font-family:"Open Sans",Arial,sans-serif;font-weight:700;color:var(--green-mid);font-size:15px;line-height:1}

.search{left:260px;top:45px;width:281px;height:28px;border:2px solid #d4d4d4;border-radius:3px;font-size:8.5px;color:#999}
.search .q{position:absolute;left:8px;top:7px}
.search .cat{position:absolute;left:167px;top:0;height:24px;border-left:1px solid #ddd;padding:7px 0 0 6px;width:84px}
.search .go{position:absolute;right:-2px;top:-2px;width:30px;height:28px;background:var(--orange);border-radius:0 3px 3px 0}

.cart{left:564px;top:44px;width:90px;height:30px}
.cart .label{position:absolute;left:32px;top:1px;font-size:7.5px;color:#555}
.cart .total{position:absolute;left:32px;top:12px;font-size:12.5px;font-weight:700;color:#444}
.cart .count{position:absolute;left:12px;top:2px;width:11px;height:11px;border-radius:50%;background:#333;color:#fff;font-size:7px;text-align:center;line-height:11px}

.hero{left:0;top:96px;width:704px;height:296px;background:linear-gradient(180deg,#5d6a5a 0%,#4a5d3f 35%,#3f6a2e 65%,#2e4d22 100%)}
.hero h1{position:absolute;left:0;top:78px;width:704px;text-align:center;font-family:"Oswald",sans-serif;font-weight:500;font-size:24px;color:var(--green);letter-spacing:.2px}
.hero p{position:absolute;left:100px;top:117px;width:504px;text-align:center;color:#fff;font-size:13px;font-weight:600;line-height:19px}
.hero .btn{position:absolute;left:290px;top:174px;width:103px;height:26px;background:#333;color:#fff;font-size:12px;text-align:center;line-height:26px;letter-spacing:.4px}

.perks{left:54px;top:390px;width:596px;height:40px;display:flex}
.perk{flex:1;position:relative;color:#fff;font-size:8px;font-weight:700;text-align:center;padding-top:16px}
.perk .ico{position:absolute;left:50%;top:-18px;margin-left:-21px;width:42px;height:32px;border-radius:21px 21px 0 0}
.perk:nth-child(1),.perk:nth-child(1) .ico{background:#8cc866}
.perk:nth-child(2),.perk:nth-child(2) .ico{background:#7cc242}
.perk:nth-child(3),.perk:nth-child(3) .ico{background:#5fac35}
.perk:nth-child(4),.perk:nth-child(4) .ico{background:#479a2a}
.perk svg{position:absolute;left:12px;top:7px}

.cats{left:54px;top:485px;width:142px;height:224px;background:var(--panel)}
.cats h2{height:22px;background:var(--green);color:#fff;font-size:8.5px;font-weight:600;padding:6px 0 0 23px;letter-spacing:.3px;position:relative}
.cats h2 i{position:absolute;left:8px;top:8px;width:9px;height:1.5px;background:#fff;box-shadow:0 3px 0 #fff,0 6px 0 #fff}
.cats ul{list-style:none;padding:0 10px}
.cats li{height:23.8px;border-bottom:1px solid #d6d6d6;font-size:7.5px;color:#333;padding-top:8px;text-transform:uppercase;letter-spacing:.2px}
.cats li:last-child{border:none}

.ad{left:54px;top:727px;width:142px;height:159px;background:linear-gradient(160deg,#fbe6d4 0%,#f6c79a 45%,#e98a3c 70%,#7fb24a 100%)}

.newsletter{left:54px;top:900px;width:142px;height:106px;background:var(--panel);padding:8px 11px}
.newsletter h3{font-size:13px;font-weight:400;color:#333}
.newsletter p{font-size:6.8px;color:#666;line-height:10px;margin-top:3px}
.newsletter .field{margin-top:6px;height:19px;background:#fff;font-size:7px;color:#777;padding:5px 7px}
.newsletter .sub{position:absolute;right:12px;top:81px;background:var(--green);color:#fff;font-size:7px;padding:3px 6px;border-radius:2px}

.banner{left:212px;top:485px;width:438px;height:88px;background:linear-gradient(90deg,#f4f4f2 0%,#f1f1ee 45%,#9bb27a 60%,#6e8a4d 75%,#e8e8e4 90%);border:1px solid #ddd}
.section-title{left:210px;top:584px;width:437px;height:26px;background:var(--green-dark);color:#fff;font-size:12px;padding:5px 0 0 11px;letter-spacing:.5px}

.card{position:absolute;width:135px;height:184px;border:1px solid var(--line);background:#fff}
.card .pic{position:absolute;left:17px;top:10px;width:100px;height:68px}
.card .tag{position:absolute;left:5px;top:4px;width:15px;height:15px;border-radius:50%;background:var(--green);color:#fff;font-size:5.5px;font-style:normal;text-align:center;line-height:15px}
.card h4{position:absolute;top:84px;width:100%;text-align:center;font-size:8.5px;font-weight:400;color:#333}
.card .desc{position:absolute;top:96px;width:100%;text-align:center;font-size:6.8px;color:#777}
.card .price{position:absolute;top:110px;width:100%;text-align:center;font-size:8.5px}
.card .price s{color:#888;margin-right:9px}
.card .price b{color:var(--red);font-weight:400;text-decoration:underline}
.card .buy{position:absolute;left:9px;top:131px;width:50px;height:18px;background:#555;color:#fff;font-size:7px;font-weight:600;text-align:center;line-height:18px}
.card .add{position:absolute;left:67px;top:131px;width:59px;height:18px;background:var(--green);color:#fff;font-size:6.5px;font-weight:600;line-height:18px;padding-left:15px}
.card .add svg{position:absolute;left:4px;top:5px}
.card hr{position:absolute;left:0;top:155px;width:100%;border:none;border-top:1px solid #f0c9c9}
.card .stars{position:absolute;left:5px;top:160px;font-size:13px;color:var(--green-mid);letter-spacing:-1px}
.card .stars em{font-style:normal;color:#c9c9c9}
.card .detail{position:absolute;right:10px;top:166px;font-size:7.5px;font-weight:600;color:#333}

.footband{left:0;top:1030px;width:704px;height:37px;background:var(--dark)}
.social{position:absolute;left:58px;top:0;width:154px;height:37px;background:var(--green);display:flex;justify-content:center;align-items:center;gap:14px}
.social i{width:8px;height:8px;border-radius:50%;background:#1f3a12}
.accepted{position:absolute;left:399px;top:10px;color:#fff;font-size:12.5px;font-weight:600}
.cards{position:absolute;left:488px;top:6px;display:flex;gap:3px}
.cards i{width:39px;height:24px;background:#fff;border-radius:2px}

.footer{left:0;top:1067px;width:704px;height:115px;background:var(--foot)}
.footer .about{position:absolute;left:60px;top:62px;width:135px;font-size:6.5px;line-height:9.5px;color:#555}
.footer .col{position:absolute;top:13px}
.footer h5{font-size:10px;font-weight:400;color:#333;margin-bottom:8px}
.footer li{list-style:none;font-size:6.3px;color:#555;height:14.5px}
.footer li::before{content:"» ";color:#777}
.contact p{font-size:6.5px;color:#555;height:12.5px;position:relative;padding-left:10px}
.contact p i{position:absolute;left:0;top:1px;width:6px;height:6px;background:#4a6fa5;border-radius:1px}
.minicards{position:absolute;left:508px;top:88px;display:flex;gap:4px}
.minicards i{width:23px;height:13px;background:#dfe3ea;border:1px solid #c8ccd4}
.copy{left:0;top:1182px;width:704px;height:18px;background:var(--foot-bottom);font-size:7px;color:#333;text-align:center;line-height:18px}
</style>
</head>
<body>

<div class="abs topbar">
  <span style="left:63px">Home</span>
  <span style="left:97px">Change Colors ⌄</span>
  <span class="sep" style="left:156px">|</span>
  <span style="left:168px">Blog</span>
  <span class="sep" style="left:190px">|</span>
  <span style="left:200px">FAQ</span>
  <span class="sep" style="left:221px">|</span>
  <span style="left:230px">Contact</span>
  <span class="sep" style="left:261px">|</span>
  <span style="left:268px">Pages ⌄</span>
  <span style="left:480px">English ⌄</span>
  <span class="sep" style="left:514px">|</span>
  <span style="left:523px">Dollar (US) ⌄</span>
  <span class="sep" style="left:571px">|</span>
  <span style="left:582px">Register</span>
  <span class="sep" style="left:613px">|</span>
  <span style="left:624px">Login</span>
</div>

<div class="abs brand" style="left:58px;top:52px">
  <div class="dot"></div>
  <div class="name">Fen Leaf Naturals</div>
</div>

<div class="abs search">
  <span class="q">Search for item</span>
  <span class="cat">All Categories ⌄</span>
  <div class="go">
    <svg width="30" height="28" viewBox="0 0 30 28"><circle cx="14" cy="13" r="5" fill="none" stroke="#fff" stroke-width="2"/><line x1="18" y1="17" x2="21" y2="20" stroke="#fff" stroke-width="2.4" stroke-linecap="round"/></svg>
  </div>
</div>

<div class="abs cart">
  <svg class="abs" style="left:0;top:6px" width="26" height="20" viewBox="0 0 26 20"><path d="M1 2h4l3 11h13l3-8H7" fill="none" stroke="#aaa" stroke-width="1.8"/><circle cx="10" cy="17" r="1.8" fill="#aaa"/><circle cx="19" cy="17" r="1.8" fill="#aaa"/></svg>
  <div class="count">3</div>
  <div class="label">Your Cart:</div>
  <div class="total">$3219,00</div>
</div>

<section class="abs hero" role="img" aria-label="Indoor growing racks full of leafy green plants under grow lights">
  <h1>FRUIT TREES FROM PENHURST ORGANIC NURSERY</h1>
  <p>The fruit tree nursery has been established to grow organic fruit trees for sale suitable for all situations from small gardens to traditional orchards.</p>
  <div class="btn">Request Now</div>
</section>

<div class="abs perks">
  <div class="perk"><div class="ico"><svg width="18" height="18" viewBox="0 0 18 18"><circle cx="9" cy="9" r="7.5" fill="none" stroke="#fff" stroke-width="1.8"/><path d="M5.5 9l2.5 2.5 4.5-5" fill="none" stroke="#fff" stroke-width="1.8"/></svg></div>1 Year Plant Gurantee</div>
  <div class="perk"><div class="ico"><svg width="18" height="18" viewBox="0 0 18 18"><path d="M7 16V6a1.5 1.5 0 013 0v4l4 1v5z" fill="#fff"/><circle cx="8.5" cy="5" r="4" fill="none" stroke="#fff" stroke-width="1.2"/></svg></div>Free Click &amp; Collect From Nursery</div>
  <div class="perk"><div class="ico"><svg width="20" height="18" viewBox="0 0 20 18"><rect x="1" y="4" width="11" height="8" fill="#fff"/><path d="M12 6h4l3 3v3h-7z" fill="#fff"/><circle cx="5" cy="14" r="2" fill="#fff"/><circle cx="15" cy="14" r="2" fill="#fff"/></svg></div>Delivery Only $4.95</div>
  <div class="perk"><div class="ico"><svg width="18" height="18" viewBox="0 0 18 18"><circle cx="9" cy="6.5" r="5" fill="none" stroke="#fff" stroke-width="1.8"/><path d="M6 11l-2 6 5-2 5 2-2-6" fill="#fff"/></svg></div>23 Gold Medals At Ashbury</div>
</div>

<nav class="abs cats">
  <h2><i></i>PRODUCT CATEGORIES</h2>
  <ul>
    <li>Pelvarimost</li>
    <li>Marsh hare soil tonic</li>
    <li>Terrawix</li>
    <li>Nuro pods</li>
    <li>Stem triumph</li>
    <li>Sprout charm</li>
    <li>Vel</li>
    <li>Flint amber</li>
  </ul>
</nav>

<div class="abs ad" role="img" aria-label="Advertisement for certified organic flower-based make-up with a flower field"></div>

<div class="abs newsletter">
  <h3>Newsletter</h3>
  <p>Lorem Ipsum is simply dummy text of the.</p>
  <div class="field">Enter Your Email</div>
  <div class="sub">Subscribe</div>
</div>

<div class="abs banner" role="img" aria-label="Organic vegetables banner with a farmer tending crops and a home delivery note"></div>

<div class="abs section-title">OUR PRODUCTS</div>

<div class="card" style="left:210px;top:624px">
  <div class="pic" role="img" aria-label="Organic skincare jars with fresh fruit" style="background:linear-gradient(135deg,#f3efe6,#e6a477 55%,#c94b3d)"></div>
  <h4>Josen maset gasten</h4><div class="desc">A long and detailed</div>
  <div class="price"><s>$32.00</s><b>$23.00</b></div>
  <div class="buy">Buy Now</div>
  <div class="add"><svg width="9" height="8" viewBox="0 0 9 8"><path d="M0 1h2l1 4h5l1-3H2.5" fill="none" stroke="#fff" stroke-width="1.1"/><circle cx="4" cy="7" r=".8" fill="#fff"/><circle cx="7" cy="7" r=".8" fill="#fff"/></svg>Add to Cart</div>
  <hr><div class="stars">★★★★<em>★</em></div><div class="detail">Detail</div>
</div>
<div class="card" style="left:361px;top:624px">
  <div class="pic" role="img" aria-label="Rolled spa towels with candles" style="background:linear-gradient(135deg,#8a6a52,#d9c8b4 50%,#6a4f3a)"><i class="tag">Sale!</i></div>
  <h4>Josen maset gasten</h4><div class="desc">A long and detailed</div>
  <div class="price"><s>$32.00</s><b>$23.00</b></div>
  <div class="buy">Buy Now</div>
  <div class="add"><svg width="9" height="8" viewBox="0 0 9 8"><path d="M0 1h2l1 4h5l1-3H2.5" fill="none" stroke="#fff" stroke-width="1.1"/><circle cx="4" cy="7" r=".8" fill="#fff"/><circle cx="7" cy="7" r=".8" fill="#fff"/></svg>Add to Cart</div>
  <hr><div class="stars">★★★★<em>★</em></div><div class="detail">Detail</div>
</div>
<div class="card" style="left:511px;top:624px">
  <div class="pic" role="img" aria-label="Wooden bowl with a purple flower" style="background:linear-gradient(135deg,#2c3038,#8a6a8c 50%,#a47a55)"></div>
  <h4>Josen maset gasten</h4><div class="desc">A long and detailed</div>
  <div class="price"><s>$32.00</s><b>$23.00</b></div>
  <div class="buy">Buy Now</div>
  <div class="add"><svg width="9" height="8" viewBox="0 0 9 8"><path d="M0 1h2l1 4h5l1-3H2.5" fill="none" stroke="#fff" stroke-width="1.1"/><circle cx="4" cy="7" r=".8" fill="#fff"/><circle cx="7" cy="7" r=".8" fill="#fff"/></svg>Add to Cart</div>
  <hr><div class="stars">★★★★<em>★</em></div><div class="detail">Detail</div>
</div>
<div class="card" style="left:210px;top:822px">
  <div class="pic" role="img" aria-label="Stone candle holder on a wooden surface" style="background:linear-gradient(135deg,#c9b8a2,#8f7a64 55%,#e2d6c6)"><i class="tag">Sale!</i></div>
  <h4>Josen maset gasten</h4><div class="desc">A long and detailed</div>
  <div class="price"><s>$32.00</s><b>$23.00</b></div>
  <div class="buy">Buy Now</div>
  <div class="add"><svg width="9" height="8" viewBox="0 0 9 8"><path d="M0 1h2l1 4h5l1-3H2.5" fill="none" stroke="#fff" stroke-width="1.1"/><circle cx="4" cy="7" r=".8" fill="#fff"/><circle cx="7" cy="7" r=".8" fill="#fff"/></svg>Add to Cart</div>
  <hr><div class="stars">★★★★<em>★</em></div><div class="detail">Detail</div>
</div>
<div class="card" style="left:361px;top:822px">
  <div class="pic" role="img" aria-label="Assorted organic product tins and boxes" style="background:linear-gradient(135deg,#f4f4f0,#5b7fb0 45%,#e4c24a 75%,#f4f4f0)"></div>
  <h4>Josen maset gasten</h4><div class="desc">A long and detailed</div>
  <div class="price"><s>$32.00</s><b>$23.00</b></div>
  <div class="buy">Buy Now</div>
  <div class="add"><svg width="9" height="8" viewBox="0 0 9 8"><path d="M0 1h2l1 4h5l1-3H2.5" fill="none" stroke="#fff" stroke-width="1.1"/><circle cx="4" cy="7" r=".8" fill="#fff"/><circle cx="7" cy="7" r=".8" fill="#fff"/></svg>Add to Cart</div>
  <hr><div class="stars">★★★★<em>★</em></div><div class="detail">Detail</div>
</div>
<div class="card" style="left:511px;top:822px">
  <div class="pic" role="img" aria-label="Herbal skincare bottles with green leaves" style="background:linear-gradient(135deg,#f5f5f0,#4f7a3a 40%,#efe6cf 75%)"></div>
  <h4>Josen maset gasten</h4><div class="desc">A long and detailed</div>
  <div class="price"><s>$32.00</s><b>$23.00</b></div>
  <div class="buy">Buy Now</div>
  <div class="add"><svg width="9" height="8" viewBox="0 0 9 8"><path d="M0 1h2l1 4h5l1-3H2.5" fill="none" stroke="#fff" stroke-width="1.1"/><circle cx="4" cy="7" r=".8" fill="#fff"/><circle cx="7" cy="7" r=".8" fill="#fff"/></svg>Add to Cart</div>
  <hr><div class="stars">★★★★<em>★</em></div><div class="detail">Detail</div>
</div>

<div class="abs footband">
  <div class="social"><i></i><i></i><i></i><i></i><i></i></div>
  <div class="accepted">We Accepted</div>
  <div class="cards"><i></i><i></i><i></i><i></i></div>
</div>

<footer class="abs footer">
  <div class="abs brand" style="left:64px;top:22px">
    <div class="dot"></div>
    <div class="name">Fen Leaf Naturals</div>
  </div>
  <p class="about">Lorem Ipsum is simply dummy text of the printing and typesetting industry. Lorem Ipsum is simply dummy text of the printing and typesetting industry.</p>
  <div class="col" style="left:223px">
    <h5>MY ACCOUNT</h5>
    <ul><li>Contact us</li><li>My Account</li><li>Checkout</li><li>View Cart</li><li>Product Listing</li></ul>
  </div>
  <div class="col" style="left:356px">
    <h5>INFORMATION</h5>
    <ul><li>About Us</li><li>Terms of Use</li><li>Club Info and FAQ's</li><li>Privacy Policy</li><li>Contact us</li></ul>
  </div>
  <div class="col contact" style="left:508px">
    <h5>CONTACT US</h5>
    <p><i></i>4120 Alder Row, Norwick, NR8 2LT</p>
    <p><i></i>Telephone: (801) 5550 - 1427</p>
    <p><i></i>E-mail: support@fenleafnaturals.co.uk</p>
  </div>
  <div class="minicards"><i></i><i></i><i></i><i></i><i></i><i></i></div>
</footer>

<div class="abs copy">Copyright © 2015 fen leaf naturals. All Rights Reserved.</div>

</body>
</html>
```